Sunscreen Package Design Modern SPF 50

Update current package design to a more modern design target women 16-40 Do not make it playful. Sol Mesa is home to movie stars and high income business people PalmSprings is one of the most desired vacation areas in the world. The sun shines 350 days a year. World class Tennis and Golf tournaments are held every year with the worlds top players attending these tournaments

Target Market(s)

Women

Industry/Entity Type

Skin Protection

Font styles to use
Sans Serif

Requirements
Must have
• The words Sol Mesa and KOVALINE

```html
<!DOCTYPE html>
<html lang="en">
<head>
<meta charset="utf-8">
<title>Sol Mesa Kovaline Sunscreen – Label</title>
<link rel="stylesheet" href="https://fonts.googleapis.com/css2?family=Inter:wght@300;400;500&family=Playfair+Display:wght@400;500&display=swap">
<style>
  :root {
    --page: #ffffff;
    --label: #ecdccb;
    --ink-dark: #2b2320;
    --ink-brown: #7a4f2a;
    --ink-copper: #9a6a3e;
    --ink-body: #4a3a30;
    --rule: #b8977a;
    --band-dark: #8a5a30;
    --band-light: #c29868;
    --scene-top: #ecdccb;
    --scene-mid: #d7bc98;
    --scene-low: #b88d60;
  }
  * { margin: 0; padding: 0; box-sizing: border-box; }
  html, body { width: 1200px; height: 550px; overflow: hidden; background: var(--page); }
  body { font-family: "Inter", Arial, sans-serif; position: relative; }

  .label {
    position: absolute; top: 26px; width: 350px; height: 497px;
    background: var(--label); overflow: hidden;
  }
  .label--front { left: 225px; }
  .label--back { left: 625px; }

  .landscape {
    position: absolute; left: 0; right: 0; top: 366px; height: 111px;
    background: linear-gradient(180deg, var(--scene-top) 0%, var(--scene-mid) 55%, var(--scene-low) 100%);
  }
  .base-band {
    position: absolute; left: 0; right: 0; bottom: 0; height: 20px;
    background: linear-gradient(90deg, var(--band-dark) 0%, var(--band-light) 50%, var(--band-dark) 100%);
  }

  /* Front */
  .front-stack { position: absolute; inset: 0; text-align: center; }
  .front-stack > * { position: absolute; left: 0; right: 0; font-weight: 400; }
  .brand-mark {
    top: 56px;
    display: flex; justify-content: center; align-items: center; gap: 6px;
    font-size: 9px; letter-spacing: 1.5px; color: var(--ink-copper);
  }
  .brand-mark__dot { width: 10px; height: 10px; border-radius: 50%; background: var(--ink-copper); }
  .place { top: 134px; font-size: 12px; line-height: 16px; color: var(--ink-brown); letter-spacing: .3px; }
  .rule-short { top: 155px; left: 152px !important; right: auto !important; width: 46px; height: 1px; background: var(--rule); }
  .product-name { top: 158px; font-family: "Playfair Display", Georgia, serif; font-size: 33px; line-height: 42px; color: var(--ink-dark); letter-spacing: .5px; }
  .rule-long { top: 211px; left: 123px !important; right: auto !important; width: 104px; height: 1px; background: var(--rule); }
  .category { top: 221px; font-size: 7.5px; line-height: 10px; color: var(--ink-dark); letter-spacing: .3px; }
  .spectrum { top: 249px; font-size: 8px; line-height: 14px; color: var(--ink-brown); letter-spacing: .3px; }
  .spf-label { top: 292px; font-size: 11px; line-height: 14px; color: var(--ink-brown); }
  .spf-value { top: 306px; font-size: 31px; line-height: 32px; font-weight: 300 !important; color: var(--ink-brown); }
  .pa-rating { top: 341px; font-size: 7px; line-height: 9px; color: var(--ink-brown); letter-spacing: .5px; }
  .water { top: 373px; font-size: 7px; line-height: 9px; color: var(--ink-dark); letter-spacing: .2px; z-index: 2; }
  .volume { top: 396px; font-size: 7px; line-height: 9px; color: var(--ink-dark); z-index: 2; }

  /* Back */
  .back-title {
    position: absolute; top: 32px; left: 0; right: 0; text-align: center;
    font-family: "Playfair Display", Georgia, serif; font-weight: 400; font-size: 16px; line-height: 21px;
    color: var(--ink-copper); letter-spacing: .3px;
  }
  .facts { position: absolute; }
  .facts--left { left: 48px; width: 124px; }
  .facts--right { left: 197px; width: 116px; }
  .facts h3 { font-weight: 400; font-size: 9.5px; line-height: 12px; color: var(--ink-dark); margin-bottom: 3px; }
  .facts p { font-size: 5.4px; line-height: 6.8px; color: var(--ink-body); }
  .facts p.contact { font-size: 7.5px; line-height: 10px; color: var(--ink-brown); margin-top: 5px; }
</style>
</head>
<body>

<section class="label label--front" aria-label="Front label">
  <div class="landscape" role="img" aria-label="Desert mountains and palm trees in warm sand tones"></div>
  <div class="front-stack">
    <div class="brand-mark"><span class="brand-mark__dot"></span><span>KOVALINE</span></div>
    <p class="place">SOL MESA</p>
    <div class="rule-short"></div>
    <h1 class="product-name">KOVALINE</h1>
    <div class="rule-long"></div>
    <p class="category">PREMIUM SUNSCREEN</p>
    <p class="spectrum">BROAD SPECTRUM<br>UVA/UVB PROTECTION</p>
    <p class="spf-label">SPF</p>
    <p class="spf-value">50</p>
    <p class="pa-rating">PA++++</p>
    <p class="water">WATER - RESISTANT (80 MINUTES)</p>
    <p class="volume">3 FL OZ / 88 mL</p>
  </div>
  <div class="base-band"></div>
</section>

<section class="label label--back" aria-label="Back label">
  <div class="landscape" role="img" aria-label="Layered desert mountains in warm sand tones"></div>
  <h2 class="back-title">SOL MESA KOVALINE<br>SUNSCREEN</h2>

  <div class="facts facts--left" style="top:98px">
    <h3>Drug Facts</h3>
    <p>Sol Mesa Kovaline Luxurious Hydration Weightless Sunscreen is a moisturizing sunscreen for protection with a light soft texture that feels weightless on the skin. Water resistant (80 minutes) Oil free, Non Greasy Dermatologist Recommended.</p>
  </div>
  <div class="facts facts--left" style="top:176px">
    <h3>Active Ingredients</h3>
    <p>Ethylhexyl Methoxycinnamate- 7.5%, Zinc Oxide- 7.5%</p>
  </div>
  <div class="facts facts--left" style="top:219px">
    <h3>Uses</h3>
    <p>Helps prevent sunburns, if used as directed with other sun protection measures</p>
  </div>
  <div class="facts facts--left" style="top:268px">
    <h3>Inactive Ingredients</h3>
    <p>Water, Glycerin, Cetearyl Alcohol, Ceteareth-20, Caprylic / capric triglyceride, Glycine Soja (Soybean) Oil, Butyrospermum Parkii (Shea Butter), Cetyl Alcohol, Glyceryl Stearate, Peg-100 Stearate, Cyclopentasiloxane, Cyclotetrasiloxane, Dimethiconol, Aloe Barbadensis Leaf Extract, Chamomilla Recutita (Matricaria) Flower Extract, Foeniculum Vulgare (Fennel) Seed Extract, Cucumis Sativus (Cucumber) Fruit Extract, Ethyl Hexyl Palmitate, Phenoxyethanol, Ethyl Hexyl Glycerin, Bisabolol, Polysorbate 20, Sodium Hyaluronate, Silica, Carbomer, Helianthus Annuus (Sunflower) Seed Oil, Simmondsia Chinensis (Jojoba) Seed Oil, Tocopheryl Acetate</p>
  </div>

  <div class="facts facts--right" style="top:98px">
    <h3>Directions</h3>
    <p>Apply liberally 15 minutes before sun exposure. Reapply: after 80 minutes of swimming or sweating; immediately after towel drying; at least every 2 hours. Sun Protection Measures: Spending time in the sun increases your risk of skin cancer and early skin aging. To decrease this risk, regularly use a sunscreen with a broad spectrum SPF value of 15 or higher and other sun protection measures including: limit time in the sun, especially from 10 a.m. - 2 p.m.; wear long-sleeved shirts, pants, hats, and sunglasses. Children under 6 months: Ask a doctor. Protect this product from excessive heat and direct sun.</p>
  </div>
  <div class="facts facts--right" style="top:231px">
    <h3>Warnings</h3>
    <p>For external use only. Do not use on damaged or broken skin. When using this product keep out of eyes. Rinse with water to remove. Stop use and ask a doctor if rash occurs. Keep out of reach of children. If product is swallowed, get medical help or contact a Poison Control Center right away. May stain some fabrics.</p>
  </div>
  <div class="facts facts--right" style="top:314px">
    <h3>Other Information</h3>
    <p>Protect this product from excessive heat and sun</p>
    <p class="contact">hello@kovaline-care.com</p>
  </div>
  <div class="base-band"></div>
</section>

</body>
</html>
```